PactLens480 Business Card Design

Design double sided premium business card – we will print on heavy card stock. Would like an edgy eye-catchcing card in Spot UV and/or Embossed or Foil. Something that will be memorable to our clients and new prospects
PLEASE NOTE: I have attached a word document with a more detailed overview, instructions and ideas. please review this and send a message if you have any questions

Industry/Entity Type

Financial Service

Contact Information for Business Card

would prefer to have Spot UV and/or Embossed or Foil (but no gold or silver- if you do foil only colored)

Requirements
Must have
• 1) Tagline: Redefining the way you search, qualify & manage vendors
• 2) Color Front of Card: Open to any color combo
• 3) Color on back of card: would prefer white so the contact information is easy to read
• 4) A creative design aspect.. the eye is an idea but not imperative. if you have another creative idea that represents pactlens480 please do so. We are open to other design ideas.
Nice to have
• If you can use the words on the card as shown on my instruction document that would be nice ... I like example 1 and 1A on the logo ideas I put on the instruction document.
Should not have
• 1) We DO NOT want an all black card. (front and back)
• 2) We do not want a basic card that has the logo on front- we want some type of design incorporated on the card. - we would like something creative to grab attention.
• Note: I have attached examples of other card designs on our instruction document we attached please review and create something eye-catching like these.

```html
<!DOCTYPE html>
<html lang="en">
<head>
<meta charset="utf-8">
<title>PactLens480 Business Card</title>
<link rel="stylesheet" href="https://fonts.googleapis.com/css2?family=Lato:wght@400;700&display=swap">
<style>
  :root {
    --backdrop: #202020;
    --front-base: #1d2430;
    --front-glow: #2f6fb8;
    --back-base: #ffffff;
    --card-edge: #2c2c2c;
    --brand-blue: #1e6fc8;
    --brand-green: #7dc242;
    --front-text: #e8eef6;
    --back-text: #2a2a2a;
    --sweep-light: #d9dde3;
    --sweep-dark: #8a929c;
  }
  * { margin: 0; padding: 0; box-sizing: border-box; }
  html, body {
    width: 1200px; height: 900px; overflow: hidden;
    background: var(--backdrop);
    font-family: "Lato", Arial, sans-serif;
  }
  .stage { position: relative; width: 1200px; height: 900px; }
  .card {
    position: absolute; left: 300px;
    width: 600px; height: 343px;
    border: 1px solid var(--card-edge);
    overflow: hidden;
  }
  .card--front { top: 70px; background: var(--front-base); }
  .card--back { top: 467px; background: var(--back-base); }

  /* Front */
  .halftone-area {
    position: absolute; left: 90px; top: 20px; width: 460px; height: 300px;
    border-radius: 50%;
    background: radial-gradient(ellipse at 60% 55%, var(--front-glow) 0%, #24466f 40%, var(--front-base) 72%);
  }
  .front-logo {
    position: absolute; left: 0; right: 0; top: 128px;
    text-align: center;
    font-size: 44px; font-weight: 700; letter-spacing: 1px;
    color: var(--front-text);
  }
  .front-tagline {
    position: absolute; left: 0; right: 0; top: 196px;
    text-align: center;
    font-size: 14px; font-weight: 400; letter-spacing: 0.5px;
    color: var(--front-text);
  }

  /* Back */
  .sweep-area { position: absolute; right: 0; top: 0; width: 360px; height: 343px; }
  .back-logo {
    position: absolute; left: 40px; top: 34px;
    display: flex; align-items: center; gap: 10px;
    font-size: 36px; font-weight: 700; color: var(--brand-blue);
  }
  .back-logo__dot { width: 14px; height: 14px; border-radius: 50%; background: var(--brand-green); }
  .contact { position: absolute; left: 40px; top: 120px; color: var(--back-text); }
  .contact__name {
    font-size: 28px; font-weight: 400; color: var(--brand-blue);
    text-transform: uppercase; letter-spacing: 1px; line-height: 1;
  }
  .contact__role { font-size: 16px; margin-top: 4px; }
  .contact__address { font-size: 15px; line-height: 1.4; margin-top: 18px; }
  .contact__list { list-style: none; margin-top: 12px; font-size: 17px; line-height: 1.45; }
  .contact__list li { display: flex; align-items: center; gap: 10px; }
  .contact__icon { width: 12px; height: 12px; flex: none; }
  .accent { color: var(--brand-blue); }
</style>
</head>
<body>
<main class="stage">
  <section class="card card--front">
    <div class="halftone-area" role="img" aria-label="Soft halftone dot pattern glowing around the name"></div>
    <div class="front-logo">PactLens480</div>
    <p class="front-tagline">Redefining the way you search, qualify &amp; manage vendors</p>
  </section>

  <section class="card card--back">
    <svg class="sweep-area" viewBox="0 0 360 343" role="img" aria-label="Embossed sweeping band rising across the card">
      <defs>
        <linearGradient id="sweep-fill" x1="0" y1="1" x2="1" y2="0">
          <stop offset="0" stop-color="var(--sweep-dark)"/>
          <stop offset="1" stop-color="var(--sweep-light)"/>
        </linearGradient>
      </defs>
      <path d="M40 343 C120 250 230 110 360 20 L360 60 C250 140 150 260 95 343 Z" fill="url(#sweep-fill)"/>
    </svg>
    <div class="back-logo"><span class="back-logo__dot"></span>PactLens480</div>
    <div class="contact">
      <h1 class="contact__name">Daniel Reyes</h1>
      <p class="contact__role">Director</p>
      <p class="contact__address">4173 N. Canyon Ridge Ave.<br>STE B-2 #318 Mesa, AZ 85201</p>
      <ul class="contact__list">
        <li>
          <svg class="contact__icon" viewBox="0 0 12 12" aria-hidden="true"><path d="M2 1h3l1 3-1.5 1a6 6 0 0 0 2.5 2.5L8 6l3 1v3a1 1 0 0 1-1 1A9 9 0 0 1 1 2a1 1 0 0 1 1-1z" fill="var(--brand-blue)"/></svg>
          (480) 555-0147
        </li>
        <li>
          <svg class="contact__icon" viewBox="0 0 12 12" aria-hidden="true"><rect x="1" y="2.5" width="10" height="7" fill="none" stroke="var(--brand-blue)" stroke-width="1.2"/><path d="M1 2.5l5 4 5-4" fill="none" stroke="var(--brand-blue)" stroke-width="1.2"/></svg>
          inquiry@pactlens480.com
        </li>
        <li>
          <svg class="contact__icon" viewBox="0 0 12 12" aria-hidden="true"><circle cx="6" cy="6" r="5" fill="none" stroke="var(--brand-blue)" stroke-width="1.2"/><path d="M1 6h10M6 1c-2.5 3-2.5 7 0 10M6 1c2.5 3 2.5 7 0 10" fill="none" stroke="var(--brand-blue)" stroke-width="1"/></svg>
          <span>www.<span class="accent">pactlens480</span>.com</span>
        </li>
      </ul>
    </div>
  </section>
</main>
</body>
</html>
```